Meadowlark Counseling Partners, LLC Needs Modern Business Card Design.

We provide behavioral health services from western Kansas to eastern Kansas. There is an abundance of competition for the services we provide with our main competitor being larger and having significantly more financial resources; however, the quality of services we provide is greater and we have started to catch the attention of the State of Kansas. We had a great logo designed by ArtFolio - this will be used to build upon our brand. The logo (attached) should be used in the card development. We want something unique, modern, but also a card design that clearly states our name, contact info, provides the name and unqiue location of each clinician, etc. Rounded edges, or a unique size, just something that makes our business card stand out from others. I have also uploaded each clinician's name and their unique location and phone number.

Our idea is to have one side be black with our logo. Then, on the other side have business cards for each individual. Plus, we want one card that is "generic" with no specific clinician's name listed so that we can give clients an appointment card when they leave. Some clinicians have two locations - we're open to design and background color, but we have started going with branding colors of black, the yellow in the logo files attached, and sometimes a gray. Our new office has been decorated using this theme.

Target Market(s)

individuals and families in need of behavioral health services; potential professional referral sources; existing referral sources

Industry/Entity Type

Business

Contact Information for Business Card

I attached a Word doc that provides clinician names, credentials and location information specific to each individual.

Font styles to use
Serif

Colors
000000
fbed22
dbdbdb
9d9d9d
c3c3c3

Requirements
Must have
• 1) use of the company logo that has been attached; 2) a template that provides us space to individualize business cards for all of our clinicians; 3) should stick to the colors we are branding with: black, yellow from the logo file, maybe a gray shade and we're open to a suggestion on a shade of white.
Nice to have
• Group discussion culminated in the thought that one side would be black with just our logo - no clinician names, etc. A unique design - rounded edges, unique size, some catchy lay-out would be nice.
Should not have
• Must not be too busy. Should look "clean." The project should stick to branding colors: black, yellow (from the logo file), maybe a gray and shade of white.

```html
<!DOCTYPE html>
<html lang="en">
<head>
<meta charset="utf-8">
<title>Meadowlark Counseling Partners – Business Card</title>
<link rel="stylesheet" href="https://fonts.googleapis.com/css2?family=Cinzel:wght@600&family=Marcellus&family=Montserrat:wght@600&family=Work+Sans:wght@400&display=swap">
<style>
  :root {
    --page: #e9e7e3;
    --card-white: #ffffff;
    --card-black: #202020;
    --brand-yellow: #f7b718;
    --ink: #3a3a3a;
    --ink-soft: #4b4b4b;
    --shadow: rgba(0, 0, 0, 0.28);
  }
  * { margin: 0; padding: 0; box-sizing: border-box; }
  html, body {
    width: 1200px; height: 1000px; overflow: hidden;
    background: var(--page);
  }
  .canvas { position: relative; width: 1200px; height: 1000px; }

  .card {
    position: absolute; left: 295px; width: 587px; height: 334px;
    box-shadow: 0 6px 14px var(--shadow);
  }
  .card--front { top: 150px; background: var(--card-white); }
  .card--back { top: 517px; background: var(--card-black); }

  .holder { position: absolute; left: 43px; top: 42px; }
  .holder__name {
    font-family: "Marcellus", serif; font-size: 24px; letter-spacing: 0.5px;
    color: var(--ink); line-height: 1;
  }
  .holder__title {
    font-family: "Montserrat", sans-serif; font-weight: 600; font-size: 15px;
    color: var(--ink-soft); margin-top: 6px;
  }

  .brand-name {
    font-family: "Cinzel", serif; font-weight: 600; color: var(--brand-yellow);
    text-align: center; line-height: 1.15;
  }
  .brand-name--front {
    position: absolute; right: 40px; top: 92px; width: 220px; font-size: 15px;
  }
  .brand-name--back {
    position: absolute; left: 0; right: 0; top: 192px; font-size: 26px;
  }
  .brand-mark {
    position: absolute; left: 50%; top: 92px; width: 74px; height: 74px;
    margin-left: -37px; border-radius: 50%; background: var(--brand-yellow);
  }

  .contact {
    position: absolute; left: 43px; top: 246px; list-style: none;
    font-family: "Work Sans", sans-serif; font-size: 13.5px; color: var(--ink);
  }
  .contact li { display: flex; align-items: center; height: 18.5px; }
  .contact svg { width: 10px; height: 10px; margin-right: 10px; fill: var(--ink); }

  .address {
    position: absolute; right: 43px; top: 266px; text-align: right;
    font-family: "Work Sans", sans-serif; font-size: 13.5px; color: var(--ink);
    font-style: normal; line-height: 15.5px;
  }
</style>
</head>
<body>
<main class="canvas">
  <section class="card card--front" aria-label="Business card front">
    <div class="holder">
      <p class="holder__name">DANIEL REEVE</p>
      <p class="holder__title">CEO</p>
    </div>
    <p class="brand-name brand-name--front">MEADOWLARK COUNSELING PARTNERS, LLC</p>
    <ul class="contact">
      <li><svg viewBox="0 0 10 10"><path d="M2.5 0h5a1 1 0 0 1 1 1v8a1 1 0 0 1-1 1h-5a1 1 0 0 1-1-1V1a1 1 0 0 1 1-1zm0.4 1.2v6.6h4.2V1.2zM5 8.3a.5.5 0 1 0 0 1 .5.5 0 0 0 0-1z"/></svg>000-123-4567</li>
      <li><svg viewBox="0 0 10 10"><path d="M2.5 0h5v3h-5zM1 3.5h8a1 1 0 0 1 1 1V7H8v3H2V7H0V4.5a1 1 0 0 1 1-1zm2 4.5v1h4V8z"/></svg>000-123-4567</li>
      <li><svg viewBox="0 0 10 10"><path d="M0 2h10v.8L5 5.8 0 2.8zM0 3.9l5 3 5-3V8.5H0z"/></svg>daniel@meadowlarkcp.com</li>
    </ul>
    <address class="address">Harvest Plaza<br>Hays Topeka</address>
  </section>

  <section class="card card--back" aria-label="Business card back">
    <span class="brand-mark" aria-hidden="true"></span>
    <p class="brand-name brand-name--back">MEADOWLARK<br>COUNSELING PARTNERS, LLC</p>
  </section>
</main>
</body>
</html>
```